依頼概要
初めまして。よろしくお願いいたします。

依頼内容
※エコー(赤ちゃん)ポスターのデザイン依頼

※エコー写真をスキャンして嵌め込みますので、そちらを想定したテンプレート型のポスターデザインをお願いいたします。

※エコーの枚数は3・6・9枚の何れかでお願いいたします。

※子供の名前 身長体重 出産時間 等

ポスターデザインのイメージや雰囲気は
デザイナー様各々におまかせしております。

```html
<!DOCTYPE html>
<html lang="ja">
<head>
<meta charset="utf-8">
<title>Baby Gift Poster</title>
<link rel="stylesheet" href="https://fonts.googleapis.com/css2?family=Bebas+Neue&family=Oswald:wght@300;400&family=Noto+Sans+JP:wght@500&display=swap">
<style>
  :root {
    --paper: #eeeeee;
    --panel: #dddddd;
    --pink: #ec6b8c;
    --ink: #1a1a1a;
    --scan-dark: #141414;
    --scan-mid: #5a5a5a;
    --white: #ffffff;
  }
  html, body { margin: 0; padding: 0; overflow: hidden; }
  body { width: 857px; height: 1200px; }
  .poster {
    position: relative;
    width: 857px;
    height: 1200px;
    background: var(--paper);
    overflow: hidden;
    font-family: "Oswald", sans-serif;
  }
  .side-panel {
    position: absolute;
    left: 429px; top: 543px;
    width: 428px; height: 657px;
    background: var(--panel);
  }
  .note-frame {
    position: absolute;
    left: 63px; top: 57px;
    width: 220px; height: 75px;
  }
  .note-lines {
    position: absolute;
    left: 76px; top: 64px;
    margin: 0;
    color: var(--pink);
    font-size: 10px;
    line-height: 12px;
    letter-spacing: 1px;
    text-transform: uppercase;
  }
  .scan {
    position: absolute;
    background: radial-gradient(ellipse at 50% 50%, var(--scan-mid) 0%, #2c2c2c 45%, var(--scan-dark) 80%);
  }
  .scan-caption {
    position: absolute;
    left: 0; right: 0;
    text-align: center;
    color: var(--white);
    font-family: "Oswald", sans-serif;
    font-weight: 400;
    letter-spacing: 1px;
  }
  .scan--small { left: 69px; width: 297px; }
  .scan--first { top: 183px; height: 237px; }
  .scan--third { top: 903px; height: 234px; }
  .scan--small .scan-caption { bottom: 10px; font-size: 14px; }
  .scan--large { left: 429px; top: 0; width: 428px; height: 543px; }
  .scan--large .scan-caption--top { top: 12px; font-size: 26px; }
  .scan--large .scan-caption--bottom { bottom: 14px; font-size: 30px; }
  .greeting {
    position: absolute;
    left: 157px; top: 500px;
    margin: 0;
    color: var(--pink);
    font-size: 24px;
    font-weight: 300;
  }
  .title {
    position: absolute;
    left: 155px; top: 532px;
    margin: 0;
    color: var(--pink);
    font-family: "Bebas Neue", sans-serif;
    font-weight: 400;
    font-size: 158px;
    line-height: 1;
    letter-spacing: 2px;
  }
  .title-rule {
    position: absolute;
    left: 157px; top: 678px;
    width: 537px; height: 5px;
    background: var(--ink);
  }
  .baby-name {
    position: absolute;
    left: 492px; top: 912px;
    margin: 0;
    color: var(--pink);
    font-family: "Noto Sans JP", sans-serif;
    font-weight: 500;
    font-size: 36px;
  }
  .baby-name .roman {
    font-family: "Oswald", sans-serif;
    font-weight: 300;
    font-size: 20px;
    margin-left: 10px;
    letter-spacing: 1px;
  }
  .birth-stats {
    position: absolute;
    left: 494px; top: 985px;
    margin: 0; padding: 0;
    list-style: none;
    color: var(--pink);
    font-weight: 300;
    font-size: 38px;
    line-height: 48px;
    letter-spacing: 2px;
  }
</style>
</head>
<body>
  <main class="poster">
    <div class="side-panel"></div>

    <svg class="note-frame" viewBox="0 0 220 75" aria-hidden="true">
      <polyline points="0,1 217,1 217,40" fill="none" stroke="var(--pink)" stroke-width="2"/>
      <polyline points="1,52 1,74 40,74" fill="none" stroke="var(--pink)" stroke-width="2"/>
    </svg>
    <p class="note-lines">welcome to our little world<br>with love from mom and dad<br>every day you grow<br>our hearts grow too</p>

    <figure class="scan scan--small scan--first" role="img" aria-label="Ultrasound scan photo slot">
      <span class="scan-caption">NOVEMBER. 30TH (2018)</span>
    </figure>

    <figure class="scan scan--large" role="img" aria-label="Ultrasound scan photo slot">
      <span class="scan-caption scan-caption--top">JULY. 27TH (2018)</span>
      <span class="scan-caption scan-caption--bottom">SEPTEMBER. 13TH (2018)</span>
    </figure>

    <p class="greeting">Happy Birthday</p>
    <h1 class="title">BABY GIFT</h1>
    <div class="title-rule"></div>

    <figure class="scan scan--small scan--third" role="img" aria-label="Ultrasound scan photo slot">
      <span class="scan-caption">NOVEMBER. 30TH (2018)</span>
    </figure>

    <h2 class="baby-name">陽菜<span class="roman">HINA</span></h2>
    <ul class="birth-stats">
      <li>3204G</li>
      <li>49.3CM</li>
      <li>AM12：12</li>
    </ul>
  </main>
</body>
</html>
```